Business card design needed

I am a nutritionist and fitness instructor and I need a business card designed for my company CookRunGrow. I provide nutrition education services such as consultations, cooking demonstrations, workshops, and supermarket tours. I also provide fitness instruction and training to clients to help overhaul their lifestyle.

I would like to see designs that have a natural, organic, feel using earthy colours. I would like to have cards printed on recycled paper.

I would prefer a 2 sided card. Front side with just the business name Cook Run Grow and underneath Nutrition Health Fitness. The second side to have the contact details.

The final design should communicate health and wellness through eating organic wholefoods and being physically active.

Although I have this idea, I would be open to see other suggestions that have a similar look and feel.

Target Market(s)

people interested in being healthier, women wanting to loose weight, mothers wanting to be healthier for their families

Industry/Entity Type

Nutrition

Contact Information for Business Card

Megan Furlow
Nutritionist and Personal Trainer
M 0417382956
E cookrungrowwellness@mailbox-demo.net

Logo Text

CookRunGrow (underneath) Nutrition Health Fitness

Logo styles of interest
Wordmark Logo
Requirements
Nice to have
• I like the idea of having the letters of CookRunGrow spelt out with food such as grains, nuts, seeds, legumes, fruit etc. For example close up images of cherry tomatoes, chia seeds, kidney beans, chickpeas, blue berries, raspberries, brown rice - lots of different colours and textures. Continuing playing on the idea of the book cover Walk Sing Rest.

food is important - I am not selling supplements rather I am promoting the enjoyment of healthy wholefoods so food is important to the look and feel of the design
Should not have
• cartoon images
images associated with body building or supplements
fruit or dumb bells with tape measures around them
clichés for weight loss such as scales and tape measures
I don't want to look like other typical wellness services such as massage or spa services

```html
<!DOCTYPE html>
<html lang="en">
<head>
<meta charset="utf-8">
<title>Cook Run Grow – Business Card</title>
<link rel="stylesheet" href="https://fonts.googleapis.com/css2?family=Jost:wght@400;600&display=swap">
<style>
  :root {
    --backdrop: #eceeed;
    --paper: #ddd9c6;
    --leaf: #2f6a2c;
    --ink: #2b2b2b;
    --ink-soft: #3d3d3d;
  }
  html, body {
    margin: 0;
    padding: 0;
    width: 878px;
    height: 1200px;
    overflow: hidden;
    background: var(--backdrop);
  }
  .canvas {
    position: relative;
    width: 878px;
    height: 1200px;
  }
  .card {
    position: absolute;
    left: 155px;
    top: 41px;
    width: 571px;
    height: 1045px;
    background: var(--paper);
    font-family: "Jost", sans-serif;
    color: var(--ink);
  }
  .brand-name {
    position: absolute;
    left: 83px;
    top: 290px;
    width: 417px;
    margin: 0;
    font-family: "Jost", sans-serif;
    font-weight: 600;
    font-size: 62px;
    line-height: 80px;
    color: var(--leaf);
    white-space: nowrap;
  }
  .rule {
    position: absolute;
    left: 83px;
    top: 545px;
    width: 417px;
    height: 3px;
    background: var(--leaf);
  }
  .tagline {
    position: absolute;
    left: 83px;
    top: 558px;
    width: 417px;
    margin: 0;
    font-weight: 600;
    font-size: 23.5px;
    letter-spacing: 0.2px;
    color: var(--leaf);
    text-transform: uppercase;
    white-space: nowrap;
  }
  .person {
    position: absolute;
    left: 83px;
    top: 684px;
    margin: 0;
  }
  .person-name {
    display: block;
    font-weight: 600;
    font-size: 25px;
    line-height: 32px;
    color: var(--ink);
  }
  .person-role {
    display: block;
    font-weight: 400;
    font-size: 26px;
    line-height: 34px;
    color: var(--ink-soft);
  }
  .contacts {
    position: absolute;
    left: 83px;
    top: 810px;
    margin: 0;
    padding: 0;
    list-style: none;
  }
  .contact {
    display: flex;
    align-items: center;
    height: 30px;
    margin-bottom: 23px;
    font-weight: 600;
    font-size: 21px;
    color: var(--ink);
    white-space: nowrap;
  }
  .contact-icon {
    width: 30px;
    height: 30px;
    margin-right: 13px;
    flex: none;
  }
</style>
</head>
<body>
<main class="canvas">
  <section class="card" aria-label="Cook Run Grow business card">
    <h1 class="brand-name">CookRunGrow</h1>
    <div class="rule"></div>
    <p class="tagline">Nutrition Education Services</p>

    <p class="person">
      <span class="person-name">Megan Furlow</span>
      <span class="person-role">Nutritionist and Personal Trainer</span>
    </p>

    <ul class="contacts">
      <li class="contact">
        <svg class="contact-icon" viewBox="0 0 30 30" aria-hidden="true">
          <rect x="8" y="2" width="14" height="26" rx="2.5" fill="none" stroke="#2b2b2b" stroke-width="2.4"/>
          <line x1="8" y1="22" x2="22" y2="22" stroke="#2b2b2b" stroke-width="2"/>
          <circle cx="15" cy="25" r="1.2" fill="#2b2b2b"/>
        </svg>
        <span>0417382956</span>
      </li>
      <li class="contact">
        <svg class="contact-icon" viewBox="0 0 30 30" aria-hidden="true">
          <rect x="2" y="7" width="26" height="17" rx="1.5" fill="none" stroke="#2b2b2b" stroke-width="2.4"/>
          <polyline points="3,8 15,18 27,8" fill="none" stroke="#2b2b2b" stroke-width="2.2"/>
        </svg>
        <span>cookrungrowwellness@mailbox-demo.net</span>
      </li>
    </ul>
  </section>
</main>
</body>
</html>
```